Open Now Poster for Retail Shop windows.

To design a poster to be printed to put on the windows of our retail stores to tell customers that we are open. Size is to be 590mm W x 840mm H supplied as a pdf. Design should incorporate our logo as well as other elements which indicate the style of our shop which is Womens Beach, Resort & Casual Clothing, Swimwear and Accessories. I would like the design to incorporate the words "Open Now" in some form in large lettering. I would also like the poster to be timeless and able to be used for other wording, so no images would be preferable.

Target Market(s)

Womens Beach, Resort & Casual Clothing, Swimwear and Accessories

Industry/Entity Type

Retail

Colors
e34297

Requirements
Must have
• words "Open Now". as well as our logo.

```html
<!DOCTYPE html>
<html lang="en">
<head>
<meta charset="utf-8">
<title>Now Open – Window Poster</title>
<link rel="stylesheet" href="https://fonts.googleapis.com/css2?family=Monoton&family=Poppins:wght@500&family=Kanit:ital,wght@1,800&display=swap">
<style>
  :root {
    --page-bg: #f1f1f1;
    --plank-light: #f3d5e6;
    --plank-mid: #eec6dc;
    --accent-pink: #e34297;
    --sun-yellow: #ffd21a;
    --frame-white: #ffffff;
  }
  * { margin: 0; padding: 0; box-sizing: border-box; }
  html, body {
    width: 1200px;
    height: 1000px;
    overflow: hidden;
    background: var(--page-bg);
  }
  .poster {
    position: absolute;
    left: 283px;
    top: 18px;
    width: 677px;
    height: 967px;
    overflow: hidden;
  }
  .poster__wood {
    position: absolute;
    inset: 0;
    background: linear-gradient(100deg, var(--plank-light) 0%, var(--plank-mid) 45%, var(--plank-light) 70%, var(--plank-mid) 100%);
  }
  .poster__frame {
    position: absolute;
    left: 79px;
    top: 99px;
    width: 504px;
    height: 766px;
    border: 13px solid var(--frame-white);
  }
  .brand-name {
    position: absolute;
    left: 0;
    right: 0;
    top: 246px;
    text-align: center;
    font-family: "Poppins", sans-serif;
    font-weight: 500;
    font-size: 24px;
    line-height: 30px;
    letter-spacing: 8px;
    text-transform: uppercase;
    color: var(--accent-pink);
  }
  .headline {
    position: absolute;
    left: 125px;
    top: 335px;
    font-family: "Monoton", cursive;
    font-weight: 400;
    font-size: 134px;
    line-height: 146px;
    color: var(--accent-pink);
    text-shadow: 5px 4px 0 var(--sun-yellow);
    transform: scaleX(0.92);
    transform-origin: left top;
    white-space: nowrap;
  }
  .headline__line { display: block; }
  .headline__line--short { letter-spacing: 18px; }
  .headline__line--long { letter-spacing: -4px; }
  .categories {
    position: absolute;
    left: 110px;
    top: 647px;
    width: 442px;
    height: 30px;
  }
  .categories__band {
    position: absolute;
    inset: 0;
    width: 100%;
    height: 100%;
  }
  .categories__text {
    position: relative;
    display: block;
    text-align: center;
    line-height: 30px;
    font-family: "Kanit", sans-serif;
    font-style: italic;
    font-weight: 800;
    font-size: 13.5px;
    color: var(--sun-yellow);
    letter-spacing: 0.4px;
    word-spacing: 2px;
  }
</style>
</head>
<body>
  <main class="poster">
    <div class="poster__wood" role="img" aria-label="Pale pink painted wooden plank background"></div>
    <div class="poster__frame"></div>

    <div class="brand-name">sea belle</div>

    <h1 class="headline">
      <span class="headline__line headline__line--short">NOW</span>
      <span class="headline__line headline__line--long">OPEN</span>
    </h1>

    <div class="categories">
      <svg class="categories__band" viewBox="0 0 442 30" preserveAspectRatio="none" aria-hidden="true">
        <polygon points="6,6 438,2 430,9 442,14 432,20 440,26 10,29 0,24 8,18 2,12" fill="var(--accent-pink)"/>
      </svg>
      <span class="categories__text">WOMENS BEACH CLOTHING &nbsp;|&nbsp; SWIMWEAR &nbsp;|&nbsp; ACCESSORIES</span>
    </div>
  </main>
</body>
</html>
```